Help create our baby! Modern facial bar website.

We want a RESPONSIVE Wordpress website that is clean, gender neutral, and modern. Mobile first is the way to go. This must look awesome on a mobile device. We are opening a modern and fresh organic mask bar with modern decor. Think clean, fresh, airy. We will also offer other services. We will offer many of the services that movie stars have access to, such as Light Therapy, Oxygen Facial, Microcurrent, Microderm, etc. Think express facial bar that is results driven. Our niche is for busy men and women who want to see results, and don't have a lot of time to spend at a spa. We are not a traditional spa. So no walking around in robes. Our services are half the cost when compared to traditional spas.

We will offer a membership program with different tiers of memberships. This is something that we want to franchise if our location is successful.

We are not into a typical spa/massage website type design with lots of commonly used images of people getting massages and facials.

We are thinking of a white background, with pops of color that are the same as our logo.

Please include the following hex codes in the website (don't think these are exact...we'd like to match the provided logo):
ea8e05
9ca0a8
14c5d4

The font of our logo is Coolvetica RG.

Target Market(s)

Young, hip, busy professionals who want to take care of their skin. Men, women, teens. Metropolitan US city.

Industry/Entity Type

Skin Care Product

Coding

Coded - Design and coding required

Font styles to use
Sans Serif

Requirements
Must have
• Modern, clean, fresh website. White background with pops of color. We need to be able to edit the text and add services through Wordpress.
Nice to have
• Pictures of men and women having fun. Some could have creams and products on their face. We want to promote facial parties. SEO is very important to us, so please design with that in mind.
Should not have
• No clip art. No cheesy pictures of women getting massages and facials. We want to avoid looking like one of the many places that do "facials" but do not really specialize in skincare. We want to avoid looking like a Nail place, or foot spa place that also does facials (so...no butterflies, leaves, and flowers).

```html
<!DOCTYPE html>
<html lang="en">
<head>
<meta charset="utf-8">
<title>Lumen Face Bar</title>
<link rel="stylesheet" href="https://fonts.googleapis.com/css2?family=Montserrat:wght@400;600;700&family=Open+Sans:ital,wght@0,400;0,600;0,700;1,400&family=Varela+Round&display=swap">
<style>
:root{
  --cyan:#14c5d4;
  --cyan-dark:#0fb3c1;
  --orange:#ea8e05;
  --orange-light:#f09a12;
  --grey:#9ca0a8;
  --ink:#333a40;
  --text:#555;
  --light:#f4f4f4;
  --footer-bar:#5a5a5a;
  --white:#fff;
}
*{box-sizing:border-box;margin:0;padding:0}
html,body{width:1200px;height:2853px;overflow:hidden}
body{font-family:"Open Sans",Arial,sans-serif;color:var(--text);background:var(--white);position:relative}
.abs{position:absolute}
.topbar{left:0;top:0;width:1200px;height:30px;background:var(--cyan);color:var(--white);font:700 13px "Montserrat",sans-serif;text-align:center;line-height:30px}
.header{left:0;top:30px;width:1200px;height:80px;background:var(--white)}
.brand{left:131px;top:22px;font:700 27px "Montserrat",sans-serif;color:var(--cyan);letter-spacing:-1px;line-height:36px;white-space:nowrap}
.nav{left:411px;top:0;width:529px;height:80px;display:flex;justify-content:space-between;align-items:center}
.nav a{font:600 11.5px "Montserrat",sans-serif;color:var(--ink);text-decoration:none;white-space:nowrap}
.btn-book{left:976px;top:27px;width:92px;height:35px;background:var(--orange);color:var(--white);font:600 13px "Montserrat",sans-serif;line-height:35px;text-align:center}
.hero{left:0;top:110px;width:1200px;height:495px;background:linear-gradient(115deg,var(--cyan) 55%,#26cedc 55%,#1fcad9 100%)}
.hero-photo{left:0;top:0;width:570px;height:495px;background:radial-gradient(ellipse at 45% 45%,#d9b6a2 0%,#c49a84 35%,rgba(20,197,212,0) 70%)}
.hero-title{left:560px;top:118px;width:507px;text-align:right;font:700 45px/56px "Montserrat",sans-serif;color:var(--white);white-space:nowrap}
.hero-text{left:670px;top:195px;width:397px;text-align:right;font:600 13px/24px "Open Sans",sans-serif;color:var(--white)}
.btn-more{left:947px;top:283px;width:120px;height:40px;background:var(--orange);color:var(--white);font:700 11.5px "Montserrat",sans-serif;line-height:40px;text-align:center}
.arrow{width:60px;height:60px;border-radius:50%;background:rgba(0,120,130,.35);top:320px}
.section-title{left:0;width:1200px;text-align:center;font:700 27px "Montserrat",sans-serif;color:var(--ink)}
.section-title span{color:var(--cyan)}
.services{left:0;top:605px;width:1200px;height:498px;background:var(--light)}
.service{width:245px;text-align:center;top:105px}
.service .pic{width:198px;height:198px;border-radius:50%;margin:0 auto;border:4px solid var(--white);box-shadow:0 0 0 1px #ddd;background:radial-gradient(circle at 55% 45%,#f4e0d6,#d8b3a3 60%,#a9cfd6)}
.service h3{font:400 20px "Varela Round",sans-serif;color:var(--orange);margin-top:26px}
.service p{font-size:11.5px;line-height:21px;color:var(--ink);margin-top:12px;padding:0 20px}
.about{left:0;top:1103px;width:1200px;height:418px;background:var(--white)}
.h-left{font:700 27px "Montserrat",sans-serif;color:var(--ink)}
.h-left span{color:var(--cyan)}
.about-text{left:133px;top:104px;width:462px;font-size:11px;line-height:20px;color:var(--ink)}
.btn-orange{background:var(--orange);color:var(--white);font:700 12px "Montserrat",sans-serif;text-align:center}
.video{left:630px;top:111px;width:439px;height:251px;background:linear-gradient(90deg,#3a3d42 0%,#6a6d72 20%,#d5d6d8 45%,#eeeeee 100%)}
.play{left:812px;top:206px}
.testimonials{left:0;top:1521px;width:1200px;height:381px;background:radial-gradient(ellipse at 30% 40%,#8a7770,#5b5553 60%,#4a4846)}
.avatar{left:203px;top:143px;width:130px;height:130px;border-radius:50%;border:4px solid var(--white);background:radial-gradient(circle,#e7c29f,#b98b62)}
.quote{left:367px;top:145px;width:710px;font:italic 400 14px/27px "Open Sans",sans-serif;color:var(--white)}
.quote-author{left:367px;top:244px;font:700 12px "Montserrat",sans-serif;color:var(--white)}
.quote-author span{font-weight:600;color:#c9c9c9;font-size:10.5px}
.plans{left:0;top:1902px;width:1200px;height:647px;background:var(--white)}
.plan{background:var(--white);box-shadow:0 0 6px rgba(0,0,0,.15);text-align:center}
.plan .name{height:57px;background:#f0f0f2;font:700 16px "Montserrat",sans-serif;color:var(--ink);line-height:57px}
.plan .price{height:122px;background:var(--cyan);color:var(--white);padding-top:18px}
.plan .amount{font:600 40px "Montserrat",sans-serif}
.plan .amount sup{font-size:17px;vertical-align:18px;margin-right:6px}
.plan .offer{font:700 12px "Montserrat",sans-serif;margin-top:10px}
.plan ul{list-style:none;padding-top:28px;font-size:12px;line-height:28px;color:var(--ink)}
.plan .signup{display:block;width:127px;height:34px;margin:23px auto 0;background:var(--cyan);color:var(--white);font:700 11.5px "Montserrat",sans-serif;line-height:34px}
.plan.featured .name,.plan.featured .price{background:var(--orange);color:var(--white)}
.plan.featured .signup{background:var(--orange)}
.footer{left:0;top:2549px;width:1200px;height:228px;background:linear-gradient(180deg,var(--orange),var(--orange-light))}
.footer h4{font:700 13.5px "Montserrat",sans-serif;color:var(--white);white-space:nowrap}
.footer p{font-size:11px;line-height:23px;color:var(--white);white-space:nowrap}
.btn-outline{border:2px solid var(--white);color:var(--white);font:700 11px "Montserrat",sans-serif;text-align:center;line-height:33px;height:37px}
.email-field{left:763px;top:77px;width:305px;height:42px;background:var(--white);font-size:10px;color:var(--ink);padding:0 13px;line-height:42px}
.email-btn{left:1027px;top:77px;width:41px;height:42px;background:#8e8e8e}
.social{width:28px;height:28px;border:2px solid var(--white);border-radius:50%}
.bottombar{left:0;top:2777px;width:1200px;height:76px;background:var(--footer-bar)}
.copyright{left:133px;top:30px;font-size:11px;color:var(--white)}
.foot-brand{left:800px;top:20px;width:268px;text-align:right;font:700 27px/36px "Montserrat",sans-serif;color:var(--white);letter-spacing:-1px;white-space:nowrap}
</style>
</head>
<body>
<div class="abs topbar">Click to Call Phone Number</div>

<header class="abs header">
  <div class="abs brand">lumen facebar</div>
  <nav class="abs nav">
    <a>FACIAL</a><a>SPA PARTIES</a><a>BOOTCAMP</a><a>PRODUCTS</a><a>ABOUT</a><a>CONTACT</a>
  </nav>
  <div class="abs btn-book">Book Now</div>
</header>

<section class="abs hero">
  <div class="abs hero-photo" role="img" aria-label="Photo of a man laughing with a clay mask on his face"></div>
  <h1 class="abs hero-title">Lumen Face Bar</h1>
  <p class="abs hero-text">Sed ut perspiciatis unde omnis iste natus error sit volu ptatemaccusantium doloremque laudantium, totamem aperiam, eaque ipsa quae ab illo inventore.</p>
  <div class="abs btn-more">READ MORE &#10148;</div>
  <svg class="abs arrow" style="left:29px" viewBox="0 0 60 60"><path d="M34 18 L22 30 L34 42" fill="none" stroke="#fff" stroke-width="2"/></svg>
  <svg class="abs arrow" style="left:1109px" viewBox="0 0 60 60"><path d="M26 18 L38 30 L26 42" fill="none" stroke="#fff" stroke-width="2"/></svg>
</section>

<section class="abs services">
  <h2 class="abs section-title" style="top:52px"><span>LUMEN</span> SERVICES</h2>
  <div class="abs service" style="left:110px"><div class="pic" role="img" aria-label="Photo of a light therapy treatment"></div><h3>Light Therapy</h3><p>Sed ut perspiciatis undiorese spt em accusantidiloreme umloreau aum, totam rem aperiausantidloremeloau dausa lorentidloreme umleam.</p></div>
  <div class="abs service" style="left:355px"><div class="pic" role="img" aria-label="Photo of an oxygen facial treatment"></div><h3>Oxygen Facial</h3><p>Sed ut perspiciatis undlome slupt em accusantidiloreme umloreau aum, totam rem aperiausantidloremeloau dausa lorentidloreme umleam.</p></div>
  <div class="abs service" style="left:600px"><div class="pic" role="img" aria-label="Photo of a microcurrent treatment"></div><h3>Microcurrent</h3><p>Sed ut perspiciatis undlore slupt em accusantidiloreme umloreau aum, totam rem aperiausantidloremeloau dausa lorentidloreme umleam.</p></div>
  <div class="abs service" style="left:845px"><div class="pic" role="img" aria-label="Photo of a microdermabrasion treatment"></div><h3>Microderm</h3><p>Sed ut perspiciatisndloreme slupt em accusantidiloreme umloreau aum, totam rem aperiausantidloremeloau dausa lorentidloreme umleam.</p></div>
</section>

<section class="abs about">
  <h2 class="abs h-left" style="left:133px;top:56px"><span>ABOUT</span> LUMEN.</h2>
  <p class="abs about-text">Lumen Face Bar was born after it's founder Dana Verlow, a busy mom of 3 decided after her last facial that she is tired of wasting hours of her day and paying exorbitant prices to have products smeared on her face with no real visible results. "I remember lying on the table having my Esthetician trying to sell me everything under the sun while smearing products on my skin (which looked great when I walked out but absolutely no difference in my skin even after regular once a month facials." quoted Dana Verlow. So for us we believe the tradition of lying in a dark room for hours is a thing of the past. We created an open facial bar offering treatments that achieve incredible outcomes. We are not like other facial spas. We offer fresh hand made products on our spa bar along with medical style services.</p>
  <div class="abs btn-orange" style="left:133px;top:325px;width:110px;height:37px;line-height:37px">READ MORE</div>
  <h2 class="abs h-left" style="left:630px;top:56px"><span>WATCH</span> OUR VIDEO</h2>
  <div class="abs video" role="img" aria-label="Video still of a woman beside a treatment light"></div>
  <svg class="abs play" width="74" height="74" viewBox="0 0 74 74"><circle cx="37" cy="37" r="33" fill="none" stroke="#fff" stroke-width="5"/><path d="M29 22 L52 37 L29 52Z" fill="#fff"/></svg>
</section>

<section class="abs testimonials" role="img" aria-label="Blurred background photo of a facial treatment">
  <h2 class="abs section-title" style="top:68px;color:#fff;font-size:26px">CLIENT TESTIMONIALS</h2>
  <svg class="abs" style="left:1052px;top:74px" width="56" height="26" viewBox="0 0 56 26"><circle cx="13" cy="13" r="11" fill="none" stroke="#fff" stroke-width="2"/><path d="M15 8 L10 13 L15 18" fill="none" stroke="#fff" stroke-width="2"/><circle cx="42" cy="13" r="11" fill="none" stroke="#999" stroke-width="2"/><path d="M40 8 L45 13 L40 18" fill="none" stroke="#999" stroke-width="2"/></svg>
  <div class="abs avatar" role="img" aria-label="Portrait photo of a smiling client"></div>
  <p class="abs quote"><b style="font-size:24px;font-style:normal">&ldquo;</b> Sed ut perspiciatis unde omnis iste natus error sit voluptatem accusantium doloremque laudantium, totam rem aperiam, eaque ipsa quae ab illo inventore veritatis et quasi architecto beatae vitae dicta sunt explicaboni mpsam voluptatem quia voluptas sit aspernatur aut odit aut fugit, sed quia consequuntur magni <b style="font-size:24px;font-style:normal">&rdquo;</b></p>
  <p class="abs quote-author">ALEX MORENO, <span>CITY NAME, LOREM SIPMDIL</span></p>
</section>

<section class="abs plans">
  <h2 class="abs section-title" style="top:40px"><span>MEMBERSHIP</span> PLANS</h2>
  <div class="abs plan" style="left:219px;top:133px;width:249px;height:422px">
    <div class="name">MEMBERSHIP1</div>
    <div class="price"><div class="amount"><sup>$</sup>9</div><div class="offer">Limited Time Offrer</div></div>
    <ul><li>Sed ut perspiciat dom</li><li>Nis iste natus error sit volu</li><li>Ptatem accusantium dol</li><li>Woremque laudantiuota</li><li>Morem aperiamue</li></ul>
    <span class="signup">SIGN UP NOW</span>
  </div>
  <div class="abs plan" style="left:732px;top:133px;width:249px;height:422px">
    <div class="name">MEMBERSHIP3</div>
    <div class="price"><div class="amount"><sup>$</sup>350</div><div class="offer">Limited Time Offrer</div></div>
    <ul><li>Sed ut perspiciat dom</li><li>Nis iste natus error sit volu</li><li>Ptatem accusantium dol</li><li>Woremque laudantiuota</li><li>Morem aperiamue</li></ul>
    <span class="signup">SIGN UP NOW</span>
  </div>
  <div class="abs plan featured" style="left:468px;top:118px;width:264px;height:453px;box-shadow:0 0 10px rgba(0,0,0,.22)">
    <div class="name" style="height:60px;line-height:60px">MEMBERSHIP2</div>
    <div class="price" style="height:132px;padding-top:10px"><div class="amount" style="font-size:58px"><sup>$</sup>46</div><div class="offer" style="margin-top:6px">Limited Time Offrer</div></div>
    <ul style="padding-top:34px"><li>Sed ut perspiciat dom</li><li>Nis iste natus error sit volu</li><li>Ptatem accusantium dol</li><li>Woremque laudantiuota</li><li>Morem aperiamue</li></ul>
    <span class="signup">SIGN UP NOW</span>
  </div>
</section>

<footer class="abs footer">
  <div class="abs" style="left:131px;top:44px"><h4>NEW BUSINESS</h4><p style="margin-top:14px">Business@lumenfacebar.com<br>hello.lumenbar.com<br>555.201.88 / 555.730.214</p></div>
  <div class="abs btn-outline" style="left:131px;top:155px;width:172px">WANT TO SUBSCRIBE US</div>
  <div class="abs" style="left:371px;top:44px"><h4>OUR ADDRESS</h4><p style="margin-top:14px">1234 Harbor ave<br>Brookfield, PA 12457</p></div>
  <div class="abs btn-outline" style="left:371px;top:155px;width:108px">VIEW MAP</div>
  <div class="abs" style="left:580px;top:44px"><h4>OPENTIME</h4><p style="margin-top:14px">8:00am -11:30am<br>2:00pm-5:30pm<br>7:00pm-10:00pm</p></div>
  <div class="abs" style="left:763px;top:44px"><h4>NEWSLETTER SIGNUP</h4></div>
  <div class="abs email-field">EMAIL:</div>
  <svg class="abs email-btn" viewBox="0 0 41 42"><rect x="13" y="15" width="15" height="11" fill="#fff"/><path d="M13 15 L20.5 21 L28 15" fill="none" stroke="#8e8e8e" stroke-width="1.5"/></svg>
  <h4 class="abs" style="left:763px;top:162px">FOLLOW US</h4>
  <div class="abs social" style="left:864px;top:155px"></div>
  <div class="abs social" style="left:896px;top:155px"></div>
  <div class="abs social" style="left:928px;top:155px"></div>
  <div class="abs social" style="left:960px;top:155px"></div>
</footer>

<div class="abs bottombar">
  <p class="abs copyright">&copy; 2016 Lumen. All Copyrights are Reserved.</p>
  <div class="abs foot-brand">lumen facebar</div>
</div>
</body>
</html>
```